SkyvornQ Business Cards and Stationary Design

Need a design for our business cards and stationary. I want to carry on the theme of the logo. I want the business cards to have a design on the back. I would like the business cards and the stationary to carry the same theme, design scheme, and branding

Target Market(s)

Airlines and Maintenance Facilities

Industry/Entity Type

Aviation

Contact Information for Business Card

Address: 4827 Tallowmere Lane, Brindlecove, Marisota, 34951

Font styles to use
Serif
Sans Serif

Colors

Designer to choose colors to be used in the design.

```html
<!DOCTYPE html>
<html lang="en">
<head>
<meta charset="utf-8">
<title>SkyvornQ Business Card</title>
<link rel="stylesheet" href="https://fonts.googleapis.com/css2?family=Roboto:wght@300;400;700&family=EB+Garamond:wght@400&display=swap">
<style>
  :root {
    --bg: #d9d9d9;
    --card: #ededed;
    --navy: #1b2d55;
    --band: #2a4d6d;
    --accent: #2a7fc8;
    --band-text: #e6ecf1;
  }
  * { box-sizing: border-box; margin: 0; padding: 0; }
  html, body { width: 1200px; height: 1200px; overflow: hidden; }
  body {
    background: var(--bg);
    font-family: "Roboto", Arial, sans-serif;
    position: relative;
  }
  .card {
    position: absolute;
    top: 360px;
    width: 480px;
    height: 480px;
    border-radius: 44px;
    background: var(--card);
    overflow: hidden;
  }
  .card-front { left: 80px; }
  .card-back { left: 640px; }

  .front-mark {
    position: absolute;
    left: 0; right: 0; top: 150px;
    display: flex;
    flex-direction: column;
    align-items: center;
    gap: 26px;
  }
  .mark-circle {
    width: 110px; height: 110px;
    border-radius: 50%;
    border: 9px solid var(--accent);
  }
  .wordmark {
    font-weight: 700;
    font-size: 52px;
    letter-spacing: 8px;
    color: var(--navy);
    text-transform: uppercase;
  }

  .back-circle {
    position: absolute;
    top: 40px; right: 44px;
    width: 56px; height: 56px;
    border-radius: 50%;
    border: 5px solid var(--accent);
  }
  .identity {
    position: absolute;
    left: 48px; top: 150px;
    color: var(--navy);
  }
  .name { font-weight: 300; font-size: 46px; line-height: 1.1; }
  .role { font-weight: 300; font-size: 26px; margin-top: 8px; padding-left: 30px; }

  .contact-band {
    position: absolute;
    left: 0; right: 0; bottom: 0;
    height: 220px;
    background: var(--band);
    padding: 34px 48px;
    font-family: "EB Garamond", Georgia, serif;
    font-size: 20px;
    line-height: 1.32;
    color: var(--band-text);
  }
  .contact-line { display: block; white-space: nowrap; }
</style>
</head>
<body>
  <section class="card card-front" aria-label="Card front">
    <div class="front-mark">
      <div class="mark-circle"></div>
      <div class="wordmark">SkyvornQ</div>
    </div>
  </section>

  <section class="card card-back" aria-label="Card back">
    <div class="back-circle"></div>
    <div class="identity">
      <div class="name">Your Name</div>
      <div class="role">Manager</div>
    </div>
    <div class="contact-band">
      <span class="contact-line">P: 555.014.2323</span>
      <span class="contact-line">P: 555.014.2323</span>
      <span class="contact-line">W: www.yourwebsite.com</span>
      <span class="contact-line">E: youremail@mailvesta.com</span>
      <span class="contact-line">4827 Tallowmere Lane,</span>
      <span class="contact-line">Brindlecove, Marisota, 34951</span>
    </div>
  </section>
</body>
</html>
```